Motivational Quotes Poster Series

This is a 3 poster design series for Ridgeway Haul Academy. The size of each poster should be 18 inches wide and 24 inches tall. The goal of these posters is to serve as motivational "signs" to be hung in the office area for the employees (not customers). These employees are instructors/teachers, teaching students how to drive semi trucks. While each design is a separate poster and design, we're posting as 1 project because we'd like some continuity between the series. Below we'll break down the details of all 3 posters...

Poster #1
Text that must appear on poster - "If You Want The Best Out Of Each Student" and "Give The Best Of You!" Note: While this text must appear on the poster, you can arrange in the layout as you see fit. For example, first line could be at top of poster and second line on bottom.

Poster #2
Text that must appear on poster - "Invest In People" and "Change Someone's Life" (same notes apply as in 1st poster)

Poster #3
Text that must appear on poster - "Today Is..." and "Just Another Day For You" and "The Most Important Day In Their Life" Note: This can be laid out on the poster however you see fit, but each phrase needs to be separate and it needs to flow.

Target Market(s)

Truck Driver Training Instructors - These are middle-aged, mostly male, masculine type personalities.

Industry/Entity Type

Training

Requirements
Must have
• Must have noted text from description
Must have working files (ie - PSD, EPS, AI, etc) provided
Must have common theme between each poster in series
Must have easy to read font and layout
Must have product dimensions of 18 inches (width) by 24 inches (height). If design uses full dimensions please include quarter inch bleed.
Nice to have
• Nice to have a trucking theme...related to trucking industry, but not over the top. Example - This could mean subtle injection of background tire tracks, but by no means are tire tracks required.

For inspiration, you can visit the site at http://www.ridgewayhaul.example. While you can use the colors of the site/logo, you can still branch out between each poster to try new colors within reason.

Note: While we've attached the logo to this project, it COULD be used but doesn't HAVE to be included in the design. The logo IS NOT a focal point. The phrases in the poster ARE the focal point.

```html
<!DOCTYPE html>
<html lang="en">
<head>
<meta charset="utf-8">
<title>Ridgeway Haul Academy — Motivational Poster Series</title>
<link rel="stylesheet" href="https://fonts.googleapis.com/css2?family=Arvo:wght@400;700&display=swap">
<style>
  :root {
    --page: #ffffff;
    --poster: #000000;
    --ink: #ffffff;
    --red: #d1232a;
    --orange: #f0913a;
    --blue: #5fa8dc;
    --wire-white: rgba(220, 220, 220, 0.28);
    --wire-orange: rgba(240, 145, 58, 0.45);
    --wire-blue: rgba(95, 168, 220, 0.4);
  }
  * { margin: 0; padding: 0; box-sizing: border-box; }
  html, body { width: 1200px; height: 720px; overflow: hidden; background: var(--page); }
  body { position: relative; font-family: "Arvo", "Rockwell", serif; font-weight: 700; color: var(--ink); }

  .poster {
    position: absolute; top: 64px; width: 348px; height: 462px;
    background: var(--poster); overflow: hidden;
  }
  .poster--invest { left: 36px; }
  .poster--best { left: 429px; }
  .poster--today { left: 820px; }

  .truck-art { position: absolute; border-radius: 40% 40% 20% 20%; }
  .poster--invest .truck-art {
    left: 0; top: 130px; width: 235px; height: 305px;
    background: radial-gradient(ellipse at 55% 60%, var(--wire-white), transparent 70%);
  }
  .poster--best .truck-art {
    left: 115px; top: 115px; width: 225px; height: 215px;
    background: radial-gradient(ellipse at 45% 55%, var(--wire-orange), transparent 70%);
  }
  .poster--today .truck-art {
    left: 0; top: 75px; width: 255px; height: 270px;
    background: radial-gradient(ellipse at 45% 50%, var(--wire-blue), transparent 70%);
  }

  .quote { position: absolute; line-height: 1; }
  .quote span { display: block; }
  .quote--right { right: 18px; text-align: right; }
  .quote--left { left: 14px; text-align: left; }

  .small { font-size: 15px; letter-spacing: 0.2px; }
  .huge { font-size: 46px; }
  .big { font-size: 29px; }
  .title { font-size: 32px; }

  .red { color: var(--red); }
  .orange { color: var(--orange); }
  .blue { color: var(--blue); }

  .brand {
    position: absolute; right: 14px; bottom: 10px;
    display: flex; align-items: center; gap: 5px;
    font-size: 8px; font-weight: 700; color: var(--ink);
  }
  .brand__mark { width: 8px; height: 8px; background: var(--red); }
</style>
</head>
<body>

  <section class="poster poster--invest">
    <div class="truck-art" role="img" aria-label="White wireframe illustration of a semi truck cab, front three-quarter view"></div>
    <h2 class="quote quote--right" style="top: 34px;">
      <span class="huge">Invest</span>
      <span class="small" style="margin-top:2px;">In People</span>
      <span class="huge red" style="margin-top:-2px;">Change</span>
      <span class="small" style="margin-top:2px;">A Student’s</span>
      <span class="huge" style="margin-top:6px;">Life</span>
    </h2>
    <div class="brand"><span class="brand__mark"></span>Ridgeway Haul Academy</div>
  </section>

  <section class="poster poster--best">
    <div class="truck-art" role="img" aria-label="Glowing orange wireframe illustration of a semi truck cab"></div>
    <h2 class="quote quote--left" style="top: 36px;">
      <span class="small">If You</span>
      <span class="big orange" style="margin-top:4px;">Want The Best</span>
      <span class="small" style="margin-top:4px;">Out Of Each</span>
      <span class="small" style="margin-top:11px;">Student…</span>
    </h2>
    <h2 class="quote quote--left" style="top: 388px;">
      <span class="big orange">Give The Best</span>
      <span class="small" style="margin-top:6px;">Of You!</span>
    </h2>
    <div class="brand"><span class="brand__mark"></span>Ridgeway Haul Academy</div>
  </section>

  <section class="poster poster--today">
    <div class="truck-art" role="img" aria-label="Blue wireframe illustration of a semi truck seen from the front"></div>
    <h2 class="quote quote--right" style="top: 26px;">
      <span class="title blue">Today Is…</span>
      <span class="small" style="margin-top:2px;">Just Another Day For You</span>
    </h2>
    <h2 class="quote quote--right" style="top: 362px;">
      <span class="small" style="font-size:16px;">The Most Important Day In…</span>
      <span class="big blue" style="margin-top:6px;">A Student’s Life</span>
    </h2>
    <div class="brand" style="left:14px; right:auto;"><span class="brand__mark"></span>Ridgeway Haul Academy</div>
  </section>

</body>
</html>
```